Book Cover for Christian Book titled, "Lamps Along the Quiet Road"

Size of book cover will be 6" x 9".
The book is about how a person can know beyond a shadow of a doubt that they will go to heaven when they die.
The Title is "Lamps Along the Quiet Road"
Subtitle is "A Plain Guide to Lasting Peace and Steady Hope for Every Season."
The front of the book should have title, subtitle, and author. The back of the book and spine should have no text and be a solid color.
The uploaded pic is a possibility for a design; but I'm open to other designs.
Whatever images are used need to be very high quality to meet Maple Print Works guidelines. Also, the finished product needs to be sized to match the MPW guide for a 6x9 book.

```html
<!DOCTYPE html>
<html lang="en">
<head>
<meta charset="utf-8">
<title>Lamps Along the Quiet Road — Front Cover</title>
<link href="https://fonts.googleapis.com/css2?family=Cinzel:wght@700;800&family=Tinos:wght@700&display=swap" rel="stylesheet">
<style>
  :root{
    --page:#e2e2e2;
    --night:#03040c;
    --deep-blue:#0b1a6a;
    --mid-blue:#2a4fb0;
    --gold-light:#f3e4b0;
    --gold:#c9ac5c;
    --gold-dark:#7e6326;
    --sub-blue:#56b8ea;
    --white:#ffffff;
  }
  *{margin:0;padding:0;box-sizing:border-box}
  html,body{width:1200px;height:960px;overflow:hidden;background:var(--page)}
  .stage{position:relative;width:1200px;height:960px}
  .cover{
    position:absolute;left:307px;top:40px;width:586px;height:880px;
    background:var(--night);overflow:hidden;
  }
  .sky-photo{
    position:absolute;inset:0;
    background:linear-gradient(180deg, var(--night) 0%, var(--deep-blue) 32%, var(--mid-blue) 56%, var(--deep-blue) 76%, var(--night) 100%);
  }
  .title{
    position:absolute;left:0;top:58px;width:100%;
    font-family:'Cinzel',serif;font-weight:800;line-height:1;
    background:linear-gradient(180deg,var(--gold-light) 0%,var(--gold) 50%,var(--gold-dark) 100%);
    -webkit-background-clip:text;background-clip:text;color:transparent;
    filter:drop-shadow(3px 4px 3px rgba(0,0,0,.7));
  }
  .title span{display:block}
  .title .line-lamps{font-size:92px;padding-left:42px}
  .title .line-along{font-size:50px;padding-left:180px;margin-top:6px}
  .title .line-quiet{font-size:96px;padding-left:60px;margin-top:4px}
  .title .line-road{font-size:58px;padding-left:230px;margin-top:2px}
  .subtitle{
    position:absolute;left:0;top:620px;width:100%;text-align:center;
    font-family:'Tinos',serif;font-weight:700;text-transform:uppercase;line-height:1.05;
  }
  .subtitle .lead{display:block;color:var(--sub-blue);font-size:34px}
  .subtitle .rest{display:block;color:var(--white);font-size:20px;margin-top:4px;letter-spacing:.5px}
  .author{
    position:absolute;left:0;top:796px;width:100%;text-align:center;
    font-family:'Tinos',serif;font-weight:700;font-size:34px;color:var(--gold);
  }
</style>
</head>
<body>
<div class="stage">
  <section class="cover">
    <div class="sky-photo" role="img" aria-label="Photograph of a bright sunrise sky with colourful clouds over calm reflective water"></div>
    <h1 class="title">
      <span class="line-lamps">Lamps</span>
      <span class="line-along">Along the</span>
      <span class="line-quiet">Quiet</span>
      <span class="line-road">Road</span>
    </h1>
    <p class="subtitle">
      <span class="lead">A Plain Guide to<br>Lasting Peace</span>
      <span class="rest">and steady hope for<br>every season.</span>
    </p>
    <p class="author">Author's Name</p>
  </section>
</div>
</body>
</html>
```